Digital Signage Slide Design – Celebrations

I am looking for a digital designer for the design of our Celebration slide for our Digital Signage solution. I have attached two basic designs (landscape & portrait) of our current celebration slide. We are wanting a completely new look and feel that delivers an inspiring layout. Your goals is to provide a design that will grab peoples attention through design and content placement. Note: the final production of the slide will have animated transitioning effects. What we require from you is the design (in PSD format) for both a Landscape (1920 x 1080) and Portrait (1080 x 1920) oriented screen and a written description of how you see the animation working.If you prefer, you can use your own mock-up content and images. What we have supplied in the example mock-up, is only example content.Please refer to the following link to view an example of what a final animated slide looks like - https://www.vidtrolla.example/watch?v=Kq7pLm20xZt If you are unsure of what a Digital Signage is, please refer to the following page on our website - https://www.brightpanels.example/industry/corporate-culture
Target Market(s)
Internal Communication Channel for Large Organisations
Colors
Designer to choose colors to be used in the design.
Look and feel
Each slider illustrates characteristics of the customer's brand and the style your logo design should communicate.

```html
<!DOCTYPE html>
<html lang="en">
<head>
<meta charset="UTF-8">
<title>Work Anniversary – Celebration Slides</title>
<link rel="stylesheet" href="https://fonts.googleapis.com/css2?family=Montserrat:wght@600;700&family=Poppins:wght@400&display=swap">
<style>
  :root {
    --page-bg: #b9b9b9;
    --teal: #3f8f98;
    --deep-blue: #2b4f86;
    --indigo: #31377a;
    --mist: #8e9ea3;
    --rust: #b4563a;
    --ink-bar: rgba(28, 30, 38, 0.88);
    --text-light: #ffffff;
    --photo-dark: #3a2a1c;
    --photo-warm: #a8773f;
  }
  * { box-sizing: border-box; margin: 0; padding: 0; }
  html, body {
    width: 883px; height: 1200px; overflow: hidden;
    background: var(--page-bg);
  }
  .board { position: relative; width: 883px; height: 1200px; }

  .slide {
    position: absolute; overflow: hidden;
    color: var(--text-light);
    text-align: center;
  }
  .slide--portrait { top: 15px; width: 415px; height: 739px; }
  .slide--portrait.slide--first { left: 16px; }
  .slide--portrait.slide--second { left: 450px; }
  .slide--landscape { left: 73px; top: 770px; width: 738px; height: 415px; }

  .slide__backdrop { position: absolute; inset: 0; }
  .slide--first .slide__backdrop {
    background:
      radial-gradient(circle at 95% 75%, rgba(180,86,58,0.75) 0, rgba(180,86,58,0) 18%),
      radial-gradient(ellipse at 20% 15%, var(--deep-blue) 0, rgba(43,79,134,0) 45%),
      radial-gradient(ellipse at 65% 55%, var(--teal) 0, rgba(63,143,152,0) 50%),
      radial-gradient(ellipse at 25% 85%, var(--indigo) 0, rgba(49,55,122,0) 50%),
      var(--mist);
  }
  .slide--second .slide__backdrop {
    background:
      radial-gradient(circle at 98% 25%, rgba(180,86,58,0.75) 0, rgba(180,86,58,0) 18%),
      radial-gradient(ellipse at 25% 15%, var(--deep-blue) 0, rgba(43,79,134,0) 45%),
      radial-gradient(ellipse at 40% 70%, var(--teal) 0, rgba(63,143,152,0) 50%),
      radial-gradient(ellipse at 85% 85%, var(--indigo) 0, rgba(49,55,122,0) 45%),
      var(--mist);
  }
  .slide--landscape .slide__backdrop {
    background:
      radial-gradient(ellipse at 78% 5%, rgba(180,86,58,0.7) 0, rgba(180,86,58,0) 18%),
      radial-gradient(ellipse at 15% 70%, var(--deep-blue) 0, rgba(43,79,134,0) 40%),
      radial-gradient(ellipse at 30% 20%, var(--teal) 0, rgba(63,143,152,0) 40%),
      radial-gradient(ellipse at 85% 60%, var(--indigo) 0, rgba(49,55,122,0) 45%),
      var(--mist);
  }

  .portrait-photo {
    position: absolute; left: 50%;
    width: 192px; height: 192px; margin-left: -96px;
    border-radius: 50%;
    border: 2px solid var(--text-light);
    background: radial-gradient(circle at 50% 60%, var(--photo-warm) 0, var(--photo-dark) 75%);
  }
  .slide--portrait .portrait-photo { top: 140px; }
  .slide--landscape .portrait-photo { top: 28px; }

  .line { position: absolute; left: 0; right: 0; line-height: 1; white-space: nowrap; }
  .honoree-name, .event-date, .event-title {
    font-family: "Montserrat", sans-serif; font-weight: 700; text-transform: uppercase;
  }
  .event-date { display: flex; justify-content: center; align-items: center; gap: 6px; font-weight: 700; }
  .event-date svg { display: block; }
  .message { font-family: "Poppins", sans-serif; font-weight: 400; }

  .slide--portrait .honoree-name { top: 369px; font-size: 25px; }
  .slide--portrait .event-date { top: 419px; font-size: 16px; }
  .slide--portrait .event-title { top: 455px; font-size: 24px; }
  .slide--portrait .message--first { top: 503px; font-size: 13.5px; }
  .slide--portrait .message--second { top: 526px; font-size: 13.5px; }

  .slide--landscape .honoree-name { top: 229px; font-size: 21px; }
  .slide--landscape .event-date { top: 263px; font-size: 13.5px; }
  .slide--landscape .event-title { top: 288px; font-size: 21px; }
  .slide--landscape .message--first { top: 317px; font-size: 13.5px; }
  .slide--landscape .message--second { top: 337px; font-size: 13.5px; }

  .info-bar {
    position: absolute; left: 0; right: 0; bottom: 0;
    background: var(--ink-bar);
    font-family: "Montserrat", sans-serif; font-weight: 600;
    font-size: 10px; display: flex; align-items: center;
  }
  .slide--portrait .info-bar { height: 44px; padding-left: 17px; }
  .slide--landscape .info-bar { height: 44px; justify-content: center; }
</style>
</head>
<body>
<main class="board">

  <section class="slide slide--portrait slide--first">
    <div class="slide__backdrop" role="img" aria-label="Watercolour texture in teal, blue and rust with rounded diamond tiles"></div>
    <div class="portrait-photo" role="img" aria-label="Portrait photo of the honoree"></div>
    <h1 class="line honoree-name">Marissa Delacourt</h1>
    <p class="line event-date">
      <svg width="15" height="15" viewBox="0 0 16 16" aria-hidden="true"><rect x="1" y="3" width="14" height="12" rx="1" fill="#fff"/><rect x="4" y="0.5" width="2" height="4" fill="#fff"/><rect x="10" y="0.5" width="2" height="4" fill="#fff"/><g fill="#3f6f88"><rect x="3" y="7" width="2.5" height="2"/><rect x="6.8" y="7" width="2.5" height="2"/><rect x="10.6" y="7" width="2.5" height="2"/><rect x="3" y="10.8" width="2.5" height="2"/><rect x="6.8" y="10.8" width="2.5" height="2"/><rect x="10.6" y="10.8" width="2.5" height="2"/></g></svg>
      10 September
    </p>
    <h2 class="line event-title">Work Anniversary</h2>
    <p class="line message message--first">Congratulations on 5 years dedicated service.</p>
    <p class="line message message--second">Thanks from all your team</p>
    <footer class="info-bar">Sed ut perspiciatis unde omnis iste natus error sit voluptatem accusantium</footer>
  </section>

  <section class="slide slide--portrait slide--second">
    <div class="slide__backdrop" role="img" aria-label="Watercolour texture in teal, blue and rust with rounded diamond tiles"></div>
    <div class="portrait-photo" role="img" aria-label="Portrait photo of the honoree"></div>
    <h1 class="line honoree-name">Marissa Delacourt</h1>
    <p class="line event-date">
      <svg width="15" height="15" viewBox="0 0 16 16" aria-hidden="true"><rect x="1" y="3" width="14" height="12" rx="1" fill="#fff"/><rect x="4" y="0.5" width="2" height="4" fill="#fff"/><rect x="10" y="0.5" width="2" height="4" fill="#fff"/><g fill="#3f6f88"><rect x="3" y="7" width="2.5" height="2"/><rect x="6.8" y="7" width="2.5" height="2"/><rect x="10.6" y="7" width="2.5" height="2"/><rect x="3" y="10.8" width="2.5" height="2"/><rect x="6.8" y="10.8" width="2.5" height="2"/><rect x="10.6" y="10.8" width="2.5" height="2"/></g></svg>
      10 September
    </p>
    <h2 class="line event-title">Work Anniversary</h2>
    <p class="line message message--first">Congratulations on 5 years dedicated service.</p>
    <p class="line message message--second">Thanks from all your team</p>
    <footer class="info-bar">Sed ut perspiciatis unde omnis iste natus error sit voluptatem accusantium</footer>
  </section>

  <section class="slide slide--landscape">
    <div class="slide__backdrop" role="img" aria-label="Watercolour texture in teal, blue and rust with rounded diamond tiles"></div>
    <div class="portrait-photo" role="img" aria-label="Portrait photo of the honoree"></div>
    <h1 class="line honoree-name">Marissa Delacourt</h1>
    <p class="line event-date">
      <svg width="12" height="12" viewBox="0 0 16 16" aria-hidden="true"><rect x="1" y="3" width="14" height="12" rx="1" fill="#fff"/><rect x="4" y="0.5" width="2" height="4" fill="#fff"/><rect x="10" y="0.5" width="2" height="4" fill="#fff"/><g fill="#3f6f88"><rect x="3" y="7" width="2.5" height="2"/><rect x="6.8" y="7" width="2.5" height="2"/><rect x="10.6" y="7" width="2.5" height="2"/><rect x="3" y="10.8" width="2.5" height="2"/><rect x="6.8" y="10.8" width="2.5" height="2"/><rect x="10.6" y="10.8" width="2.5" height="2"/></g></svg>
      10 September
    </p>
    <h2 class="line event-title">Work Anniversary</h2>
    <p class="line message message--first">Congratulations on 5 years dedicated service.</p>
    <p class="line message message--second">Thanks from all your team</p>
    <footer class="info-bar">Sed ut perspiciatis unde omnis iste natus error sit voluptatem accusantium</footer>
  </section>

</main>
</body>
</html>
```